Global social media analytics company needs business card design

We need an updated business card design to align with our new website - plumvantix.com -

I would also like a favicon designed as well.

Target Market(s)

CEOs, CMOs go big companies

Industry/Entity Type

Business

Contact Information for Business Card

Room for the following:
Address
Main telephone
Direct telephone or cell phone
twitter handle

Colors
aaaaaa

Requirements
Must have
• Attention to detail; style.
• Use the logo color from our website - which is gray

```html
<!DOCTYPE html>
<html lang="en">
<head>
<meta charset="utf-8">
<title>Plumvantix Business Card</title>
<link href="https://fonts.googleapis.com/css2?family=Arimo:wght@400;700&display=swap" rel="stylesheet">
<style>
  :root {
    --brand-gray: #aaaaaa;
    --band-dark: #606163;
    --card-white: #ffffff;
    --rule-gray: #b3b3b3;
    --ink: #1f1f1f;
    --backdrop: #e9e7e4;
    --card-edge: #8a8a8a;
  }
  * { margin: 0; padding: 0; box-sizing: border-box; }
  html, body {
    width: 1173px; height: 1200px; overflow: hidden;
    background: var(--backdrop);
    font-family: "Arimo", Arial, sans-serif;
  }
  .sheet { position: relative; width: 1173px; height: 1200px; }
  .card {
    position: absolute; left: 134px; width: 877px; height: 501px;
    background: var(--card-white);
    border: 1px solid var(--card-edge);
    overflow: hidden;
  }
  .card--front { top: 78px; }
  .card--back { top: 620px; }

  .brand {
    position: absolute; display: flex; align-items: center; gap: 22px;
  }
  .brand__dot { border-radius: 50%; background: var(--brand-gray); flex: none; }
  .brand__name { color: var(--brand-gray); font-weight: 700; line-height: 1; }
  .card--front .brand { left: 151px; top: 86px; }
  .card--front .brand__dot { width: 148px; height: 148px; }
  .card--front .brand__name { font-size: 64px; }

  .card--back .brand { left: 0; right: 0; top: 0; bottom: 0; justify-content: center; gap: 28px; }
  .card--back .brand__dot { width: 170px; height: 170px; }
  .card--back .brand__name { font-size: 72px; }

  .rule { position: absolute; left: 0; right: 0; top: 313px; height: 2px; background: var(--rule-gray); }

  .identity {
    position: absolute; left: 0; top: 322px; width: 407px; bottom: 0;
    background: var(--band-dark); color: #fff;
    padding: 14px 0 0 34px;
  }
  .identity__name { font-size: 28px; font-weight: 700; line-height: 1.2; }
  .identity__title { font-size: 22px; font-weight: 400; }
  .identity__company { margin-top: 22px; font-size: 22px; font-weight: 700; line-height: 1.2; }
  .identity__address { font-size: 22px; line-height: 29px; margin-top: 4px; }

  .contacts {
    position: absolute; left: 407px; right: 0; top: 322px; bottom: 0;
    background: var(--brand-gray); color: var(--ink);
    list-style: none; padding: 12px 0 0 48px;
  }
  .contacts__item { display: flex; align-items: center; gap: 10px; height: 42px; font-size: 23px; }
  .contacts__icon { width: 20px; height: 22px; flex: none; fill: var(--ink); }
  .contacts__mark { width: 18px; height: 18px; border-radius: 50%; background: #2a9fd8; flex: none; margin: 0 1px; }
</style>
</head>
<body>
<main class="sheet">
  <section class="card card--front">
    <div class="brand">
      <span class="brand__dot"></span>
      <span class="brand__name">plumvantix</span>
    </div>
    <div class="rule"></div>
    <div class="identity">
      <p class="identity__name">Your Name, <span class="identity__title">Title</span></p>
      <p class="identity__company">PLUMVANTIX, INC.</p>
      <p class="identity__address">782 Linden Park Rd. 3rd Fl<br>Northvale, MA 01987, USA</p>
    </div>
    <ul class="contacts">
      <li class="contacts__item">
        <svg class="contacts__icon" viewBox="0 0 20 22" aria-hidden="true"><circle cx="10" cy="11" r="9" fill="none" stroke="#1f1f1f" stroke-width="1.5"/><path d="M7 6c-1 1-1 3 1 6s4 4 5 3l1-1-2-2-1 1c-1-0.5-2-2-2.5-3l1-1-2-2z"/></svg>
        <span>+1 555 310 4826</span>
      </li>
      <li class="contacts__item">
        <svg class="contacts__icon" viewBox="0 0 20 22" aria-hidden="true"><rect x="4" y="4" width="12" height="17" rx="2"/><rect x="6" y="6" width="8" height="5" fill="#aaaaaa"/><rect x="6" y="0" width="2" height="5"/></svg>
        <span>+123 456 7890</span>
      </li>
      <li class="contacts__item">
        <svg class="contacts__icon" viewBox="0 0 20 22" aria-hidden="true"><rect x="1" y="5" width="18" height="13" rx="1.5"/><path d="M2 6l8 6 8-6" fill="none" stroke="#aaaaaa" stroke-width="1.6"/></svg>
        <span>info@plumvantix.com</span>
      </li>
      <li class="contacts__item">
        <span class="contacts__mark"></span>
        <span>@plumvantix</span>
      </li>
    </ul>
  </section>

  <section class="card card--back">
    <div class="brand">
      <span class="brand__dot"></span>
      <span class="brand__name">plumvantix</span>
    </div>
  </section>
</main>
</body>
</html>
```